Coffeeshop menu for filter tip

We want to have a cannabis (coffeeshop) menu in the size 25mm wide x 60mm wide. Some examples attached.

it must have the following text:
Menu

WEED p/g
Velotrine €16
Cinderfox €14
Tide Rambler €14
Marigolden €16
Grand Pelican €14
Copper Comet €14

HASH p/g
Baltic Ember €12
Harbor Velvet€11
Plum Rova €14
Dusk Maple €10

Target Market(s)

tourist in Amsterdam

Requirements
Nice to have
• cannabis sign leaf
• No Cigarettes allowed symbol

```html
<!DOCTYPE html>
<html lang="en">
<head>
<meta charset="utf-8">
<title>Coffeeshop Menu</title>
<link href="https://fonts.googleapis.com/css2?family=Gochi+Hand&display=swap" rel="stylesheet">
<style>
  :root {
    --page: #ffffff;
    --card: #41368f;
    --card-deep: #372d80;
    --chalk: #f4f1f6;
    --cloud: #f7f5f8;
    --accent: #e2461f;
    --ink: #1d1830;
  }
  * { margin: 0; padding: 0; box-sizing: border-box; }
  html, body {
    width: 1200px; height: 1200px; overflow: hidden;
    background: var(--page);
  }
  .menu-card {
    position: absolute; left: 375px; top: 78px;
    width: 438px; height: 1050px;
    background: radial-gradient(ellipse at 50% 50%, var(--card) 0%, var(--card-deep) 100%);
    font-family: "Gochi Hand", cursive;
    color: var(--chalk);
    overflow: hidden;
  }
  .title-art-left {
    position: absolute; left: 8px; top: 60px; width: 80px; height: 60px;
    border-radius: 30px; background: var(--accent); opacity: .8;
  }
  .title-art-right {
    position: absolute; left: 290px; top: 105px; width: 105px; height: 50px;
    border-radius: 25px; background: var(--accent); opacity: .8;
  }
  .menu-title {
    position: absolute; left: 0; top: 22px; width: 438px;
    text-align: center;
    font-size: 104px; line-height: 1; letter-spacing: 4px;
    color: var(--chalk);
    text-shadow: -5px 4px 0 var(--ink);
  }
  .section-head { position: absolute; left: 0; width: 438px; height: 94px; }
  .section-head svg { position: absolute; left: 0; top: 0; }
  .section-label {
    position: absolute; left: 55px; top: 20px;
    font-size: 50px; color: var(--accent); letter-spacing: 2px; line-height: 1;
  }
  .unit-label {
    position: absolute; left: 336px; top: 24px;
    font-size: 42px; color: var(--accent); line-height: 1;
  }
  .price-list { list-style: none; }
  .price-list li {
    position: absolute; left: 31px; width: 380px;
    display: flex; justify-content: space-between; align-items: baseline; gap: 12px;
    font-size: 36px; line-height: 1; text-transform: uppercase; letter-spacing: 0;
    white-space: nowrap;
    transform: translateY(-50%);
  }
  .price { font-size: 34px; flex: none; }
  .rules { position: absolute; left: 0; top: 962px; width: 438px; height: 70px; }
  .tea-art {
    position: absolute; left: 348px; top: 967px; width: 56px; height: 60px;
    border-radius: 8px; background: rgba(244,241,246,.25);
  }
</style>
</head>
<body>
<main class="menu-card">
  <div class="title-art-left" role="img" aria-label="Orange crayon patch with cannabis leaf sketch"></div>
  <div class="title-art-right" role="img" aria-label="Orange crayon patch with sketched hand holding a joint"></div>
  <h1 class="menu-title">MENU</h1>

  <section class="section-head" style="top:163px">
    <svg width="438" height="94" viewBox="0 0 438 94" aria-hidden="true">
      <rect x="22" y="4" width="230" height="86" rx="40" fill="var(--cloud)"/>
      <path d="M252 40 q10 -8 20 0 t20 0 t20 0 t14 0 M252 56 q10 8 20 0 t20 0 t20 0 t14 0" fill="none" stroke="var(--chalk)" stroke-width="1.5"/>
      <rect x="318" y="2" width="92" height="90" rx="40" fill="var(--cloud)"/>
    </svg>
    <span class="section-label">WEED</span>
    <span class="unit-label">P/g</span>
  </section>

  <ul class="price-list">
    <li style="top:290px"><span>Velotrine</span><span class="price">€ 16</span></li>
    <li style="top:346px"><span>Cinderfox</span><span class="price">€ 14</span></li>
    <li style="top:402px"><span>Tide Rambler</span><span class="price">€ 14</span></li>
    <li style="top:458px"><span>Marigolden</span><span class="price">€ 16</span></li>
    <li style="top:516px"><span>Grand Pelican</span><span class="price">€ 14</span></li>
    <li style="top:574px"><span>Copper Comet</span><span class="price">€ 14</span></li>
  </ul>

  <section class="section-head" style="top:616px">
    <svg width="438" height="94" viewBox="0 0 438 94" aria-hidden="true">
      <rect x="22" y="4" width="230" height="86" rx="40" fill="var(--cloud)"/>
      <path d="M252 36 l9 8 l9 -8 l9 8 l9 -8 l9 8 l9 -8 l9 8 l9 -8 l8 8 M252 58 l9 -8 l9 8 l9 -8 l9 8 l9 -8 l9 8 l9 -8 l9 8 l8 -8" fill="none" stroke="var(--chalk)" stroke-width="1.5"/>
      <rect x="318" y="2" width="92" height="90" rx="40" fill="var(--cloud)"/>
    </svg>
    <span class="section-label">HASH</span>
    <span class="unit-label">P/g</span>
  </section>

  <ul class="price-list">
    <li style="top:750px"><span>Baltic Ember</span><span class="price">€ 12</span></li>
    <li style="top:806px"><span>Harbor Velvet</span><span class="price">€ 11</span></li>
    <li style="top:862px"><span>Plum Rova</span><span class="price">€ 14</span></li>
    <li style="top:918px"><span>Dusk Maple</span><span class="price">€ 10</span></li>
  </ul>

  <svg class="rules" width="438" height="70" viewBox="0 0 438 70" aria-label="No smoking and cannabis symbols">
    <g transform="translate(61 35)">
      <circle r="29" fill="none" stroke="#fff" stroke-width="6"/>
      <rect x="-17" y="-3" width="28" height="7" fill="#fff"/>
      <rect x="13" y="-3" width="4" height="7" fill="#fff"/>
      <path d="M12 -6 q-2 -6 3 -10" fill="none" stroke="#fff" stroke-width="2"/>
      <line x1="-20" y1="-20" x2="20" y2="20" stroke="#fff" stroke-width="6"/>
    </g>
    <g transform="translate(224 35)">
      <circle r="29" fill="none" stroke="#fff" stroke-width="6"/>
      <circle r="14" fill="rgba(255,255,255,.85)" role="img" aria-label="Cannabis leaf"/>
    </g>
  </svg>
  <div class="tea-art" role="img" aria-label="Drawing of a teacup with cannabis leaves"></div>
</main>
</body>
</html>
```